IT consulting company looking for a modern business design for a website and a new logo

We are the IT-consulting company VelTarix from Germany and need a new and modern business website and a new logo. We are specialized in output management. Our services include business analysis, outsourcing, development, training and project leading. We wish for a design with nature pictures (mountains, lakes, rivers, forests, etc.) for our company with the colors green and blue. If it is possible, a slow-mo video of a nature scene. The design should be responsive and the menu should change to a hamburger menu. The following are: • Services / Solutions 1. Output Management 2. Outsourcing 3. Development 4. Business Analyst 5. Training • Partners • Careers • About Us 1. Project A 2. Project B 3. Project C • Contact Notes for the following categories: For "Services / Solutions" we want to conclude some contents from all the sub-points and sub-points below. Additionally, we would like to see some sub-point under "Services / Solutions". For Output Management: "5 Benefits of Output Management Systems (OMS) - OMS Simplifies and Accelerates External Communication - Helps Reduce Communication Mistakes - Provides Customers With Fast and Secure Responses to your questions - Employees can focus on the essential as they can access prepared templates - Companies get complete transparency about their communication "The point" partner does not have sub-points. The content here is a quote and the logo from the company Brin. For now, just placeholders on this site. The next point wants to be "career" without sub-point and wants to contain some text. Carrer options wants to be listed here. Next point wants to be "About us", where we need sub-points which we do not know exactly at this moment, but they will contain text. By clicking directly on "About us" we want to include pictures and texts about 6 employees for which we only need placeholders at the moment. The last point wants to be "contact", where customers can send us messages. The main page should include a story about our company, which can be a placeholder for now. For reference, designs have a look at: https://lumoravex.de/ https://www.trobelink.com/ https://www.pemdarix.de/ We prefer WordPress designs, created with the plugin ELEMENTOR, so that we can easily edit the content by ourselves. The final design should look professional, competent and modern.

Target Market(s)

With our website, we want to reach the following target groups. <br> <br> <br> <br> <br> <br> <br> <br> <br> <br> <br> <br> <br> <br> <br> <br> <br> <br> <br> <br> <br> <br> <br> <br> <br> <br> <br> <br> <br> <br> <br> <br> <br> <br> <br> <br> <br> <br> <br> <br> <br> <br> <br> <br> <br> <br> <br> <br> <br>

Industry/Entity Type

Consulting

Logo Text

(optionally) VelTarix

Font styles to use
Sans Serif

Colors

Designer to choose colors to be used in the design.

Requirements
Must have
• 1. Outsourcing 3. Development 4. Business Analyst 5. Training • Partners • Careers • About Us 1. Project A 2. Project B 3. Project C • Contact The above-mentioned background picture with nature motifs (mountains, lakes, rivers, forests, etc.). WordPress design in primary colors blue and green.
Nice to have
• ELEMENTOR template. Effects for the background pictures. Counter of all successful projects for Output Management, Business Analyst and Training

```html
<!DOCTYPE html>
<html lang="en">
<head>
<meta charset="utf-8">
<title>VelTarix – IT Consulting</title>
<link href="https://fonts.googleapis.com/css2?family=Montserrat:wght@300;400;500;600;700&family=Open+Sans:wght@400;600;700&display=swap" rel="stylesheet">
<style>
:root{
  --green:#27ae68;
  --green-dark:#1f9a5a;
  --blue:#1363f5;
  --blue-bright:#0d5cff;
  --ink:#333;
  --muted:#666;
  --light:#e9f3f7;
  --footer:#2b2b2b;
  --footer-text:#bbb;
  --white:#fff;
  --badge:#c9c9c9;
}
*{box-sizing:border-box;margin:0;padding:0}
html,body{width:1200px;height:4016px;overflow:hidden}
body{font-family:"Open Sans",Arial,sans-serif;color:var(--ink);background:var(--white);position:relative}
h1,h2,h3,h4{font-family:"Montserrat",Arial,sans-serif;font-weight:400}
.btn{display:inline-block;background:var(--blue);color:var(--white);font-family:"Montserrat",sans-serif;font-size:11px;font-weight:600;letter-spacing:.5px;padding:10px 18px;text-decoration:none}
.btn--ghost{background:var(--white);color:var(--green)}
.section-title{font-size:32px;text-align:center}
.lead{font-size:12.5px;line-height:1.6;color:var(--muted);text-align:center;width:960px;margin:0 auto}

/* header */
.site-header{height:88px;display:flex;align-items:center;justify-content:space-between;padding:0 140px}
.brand{font-family:"Montserrat",sans-serif;font-size:34px;font-weight:500;color:#222;letter-spacing:.5px}
.nav{display:flex;gap:26px;list-style:none;font-family:"Montserrat",sans-serif;font-size:11px;font-weight:500}
.nav a{color:var(--muted);text-decoration:none}
.nav .active a{color:var(--blue);border-bottom:2px solid var(--blue);padding-bottom:6px}

/* hero */
.hero{position:relative;height:512px;background:linear-gradient(180deg,#6f8f7a 0%,#3f6a55 30%,#2f5a63 55%,#4b6f7d 75%,#2a3f48 100%);color:var(--white);text-align:center}
.hero__play{position:absolute;left:577px;top:290px}
.hero__title{position:absolute;top:362px;width:100%;font-size:28px;font-weight:400}

/* welcome */
.welcome{height:320px;padding-top:74px;text-align:center}
.welcome .section-title{color:var(--green);margin-bottom:12px}
.welcome .btn{margin-top:22px}

/* services */
.services{position:relative;height:720px;background:var(--green);color:var(--white)}
.services__title{position:absolute;left:140px;top:80px;font-size:64px;font-weight:600}
.service-list{position:absolute;left:140px;top:170px;list-style:none}
.service-list li{display:flex;align-items:center;gap:14px;font-family:"Montserrat",sans-serif;font-size:30px;font-weight:300;height:62px}
.service-list li.current{font-weight:500}
.services__media{position:absolute;left:522px;top:178px;width:540px;height:242px;background:linear-gradient(135deg,#5b6a78,#8c9aa5 45%,#3d4b58)}
.services__media svg{position:absolute;left:245px;top:96px}
.benefits{position:absolute;left:522px;top:440px;list-style:none;font-size:11.5px;line-height:2.2}
.benefits li::before{content:"";display:inline-block;width:4px;height:4px;background:var(--white);border-radius:50%;margin-right:10px;vertical-align:middle}
.services .btn{position:absolute;left:522px;top:608px}

/* partner */
.partner{position:relative;height:600px;text-align:center;padding-top:88px}
.partner .section-title{color:var(--green);margin-bottom:16px}
.quote{font-size:13px;line-height:1.6;color:var(--muted);width:900px;margin:0 auto;font-style:italic}
.quote__author{color:var(--blue);font-size:13px;font-weight:600;margin-top:10px}
.partner__arrow{position:absolute;top:178px}
.badges{display:grid;grid-template-columns:repeat(7,96px);column-gap:40px;row-gap:14px;justify-content:center;margin-top:40px}
.badge{height:18px;background:var(--badge);border-radius:2px}
.badge:nth-child(3n){width:60px;margin:0 auto}
.badge:nth-child(4n+1){width:80px;margin:0 auto}

/* career */
.career{height:520px;background:var(--light);padding-top:70px;text-align:center}
.career .section-title{color:var(--green);margin-bottom:12px}
.jobs{display:flex;gap:14px;justify-content:center;margin-top:22px;text-align:left}
.job{width:168px;height:184px;background:var(--white);padding:12px 12px}
.job h4{font-size:14px;color:var(--green)}
.job:nth-child(even) h4{color:var(--blue)}
.job h5{font-size:10px;font-weight:700;margin:4px 0 10px}
.job p{font-size:9.5px;line-height:1.6;color:var(--muted)}
.job a{display:block;margin-top:12px;font-size:10px;font-weight:700;color:var(--blue);text-decoration:none}
.career .btn{margin-top:30px}

/* about */
.about{height:560px;text-align:center;padding-top:72px}
.about .section-title{color:var(--green);margin-bottom:12px}
.about .btn{margin-top:22px}
.staff-title{font-size:22px;margin:30px 0 14px}
.staff{display:flex;gap:22px;justify-content:center}
.member{width:138px}
.member__photo{height:150px;background:linear-gradient(180deg,#b9b4ad,#7d746c)}
.member__name{color:var(--blue);font-size:11px;font-weight:600;margin-top:10px}
.member__role{font-size:9px;color:var(--muted)}

/* contact */
.contact{height:440px;background:var(--blue-bright);text-align:center;padding-top:88px;color:var(--white)}
.contact .section-title{margin-bottom:26px}
.form{width:920px;margin:0 auto}
.form__row{display:flex;gap:20px}
.field{flex:1;height:34px;background:var(--white);color:#999;font-size:10px;text-align:left;padding:10px}
.field--msg{height:120px;margin-top:20px}
.contact .btn{background:var(--white);color:var(--blue);margin-top:18px}

/* footer */
.site-footer{position:relative;height:256px;background:var(--footer);color:var(--footer-text);font-size:10px}
.site-footer h4{color:var(--white);font-size:16px;margin-bottom:12px}
.footer-col{position:absolute;top:36px;line-height:1.9}
.links{display:grid;grid-template-columns:70px 70px}
.social{display:flex;gap:8px}
.social span{width:22px;height:22px;border-radius:50%;background:var(--blue)}
.copyright{position:absolute;bottom:22px;width:100%;text-align:center;font-size:9px}
</style>
</head>
<body>

<header class="site-header">
  <div class="brand">VelTarix</div>
  <ul class="nav">
    <li class="active"><a href="#">ABOUT US</a></li>
    <li><a href="#">SERVICES</a></li>
    <li><a href="#">PARTNERS</a></li>
    <li><a href="#">CAREER</a></li>
    <li><a href="#">CONTACT</a></li>
  </ul>
</header>

<section class="hero" role="img" aria-label="Mountain lake between green forested slopes, slow-motion nature video">
  <svg class="hero__play" width="46" height="46" viewBox="0 0 46 46"><circle cx="23" cy="23" r="22" fill="#fff"/><path d="M18 14l14 9-14 9z" fill="#2f5a63"/></svg>
  <h1 class="hero__title">Praesent scelerisque fermentum mauris</h1>
</section>

<section class="welcome">
  <h2 class="section-title">Welcome to VelTarix</h2>
  <p class="lead">We help companies shape clear, fast and secure customer communication. Since our founding we have guided teams through analysis, development and rollout of output management systems, always with an eye on quality and long-term value. Our consultants combine technical depth with practical experience, so projects stay on time and on budget. Get to know our story and the people who make it.</p>
  <a class="btn" href="#">READ MORE</a>
</section>

<section class="services">
  <h2 class="services__title">Services</h2>
  <ul class="service-list">
    <li><svg width="24" height="24" viewBox="0 0 24 24" fill="none" stroke="#fff" stroke-width="2"><path d="M3 21h18M6 17v-6M12 17V5M18 17v-9"/></svg>Business Analysis</li>
    <li><svg width="24" height="24" viewBox="0 0 24 24" fill="none" stroke="#fff" stroke-width="2"><circle cx="8" cy="8" r="3"/><circle cx="16" cy="8" r="3"/><path d="M2 20c0-4 3-6 6-6s6 2 6 6M12 20c0-4 2-6 4-6s6 2 6 6"/></svg>Outsourcing</li>
    <li><svg width="24" height="24" viewBox="0 0 24 24" fill="none" stroke="#fff" stroke-width="2"><path d="M8 6l-6 6 6 6M16 6l6 6-6 6"/></svg>Development</li>
    <li><svg width="24" height="24" viewBox="0 0 24 24" fill="none" stroke="#fff" stroke-width="2"><rect x="3" y="4" width="18" height="12"/><path d="M12 16v5M8 21h8"/></svg>Trainings</li>
    <li class="current"><svg width="24" height="24" viewBox="0 0 24 24" fill="none" stroke="#fff" stroke-width="2"><path d="M5 22V3M5 4h13l-3 4 3 4H5"/></svg>Project Leading</li>
  </ul>
  <div class="services__media" role="img" aria-label="Video still of a consultant working at a laptop">
    <svg width="50" height="50" viewBox="0 0 50 50"><circle cx="25" cy="25" r="24" fill="#fff"/><path d="M20 15l15 10-15 10z" fill="#3d4b58"/></svg>
  </div>
  <ul class="benefits">
    <li>OMS simplifies and speeds up communication with the outside world</li>
    <li>Helps to reduce errors in communication</li>
    <li>Customers receive quick and secure answers to their questions</li>
    <li>Employees can focus on the essential as they can access prepared templates</li>
    <li>Companies get complete transparency about their communication</li>
  </ul>
  <a class="btn btn--ghost" href="#">READ MORE</a>
</section>

<section class="partner">
  <h2 class="section-title">Partner</h2>
  <p class="quote">“ Working with this team changed how we talk to our customers. Every letter, invoice and notice now leaves our systems faster and with fewer mistakes, and our staff finally has time for the work that really matters. We look forward to the next steps together. ”</p>
  <p class="quote__author">Mara Fendel, Ostrava Group</p>
  <svg class="partner__arrow" style="left:56px" width="14" height="22" viewBox="0 0 14 22"><path d="M12 2L3 11l9 9" fill="none" stroke="#999" stroke-width="2"/></svg>
  <svg class="partner__arrow" style="right:56px" width="14" height="22" viewBox="0 0 14 22"><path d="M2 2l9 9-9 9" fill="none" stroke="#999" stroke-width="2"/></svg>
  <div class="badges" role="list" aria-label="Partner badges">
    <div class="badge"></div><div class="badge"></div><div class="badge"></div><div class="badge"></div><div class="badge"></div><div class="badge"></div><div class="badge"></div>
    <div class="badge"></div><div class="badge"></div><div class="badge"></div><div class="badge"></div><div class="badge"></div><div class="badge"></div><div class="badge"></div>
    <div class="badge"></div><div class="badge"></div><div class="badge"></div><div class="badge"></div><div class="badge"></div><div class="badge"></div><div class="badge"></div>
    <div class="badge"></div><div class="badge"></div><div class="badge"></div><div class="badge"></div><div class="badge"></div><div class="badge"></div><div class="badge"></div>
    <div class="badge"></div><div class="badge"></div><div class="badge"></div><div class="badge"></div><div class="badge"></div><div class="badge"></div><div class="badge"></div>
    <div class="badge"></div><div class="badge"></div><div class="badge"></div><div class="badge"></div><div class="badge"></div><div class="badge"></div><div class="badge"></div>
  </div>
</section>

<section class="career">
  <h2 class="section-title">Career</h2>
  <p class="lead">We are always looking for curious people who enjoy solving problems with customers. Join a friendly team, work on meaningful projects across Germany and grow with training, mentoring and flexible hours. Browse our open positions below and send us your application today. We look forward to meeting you and hearing your ideas.</p>
  <div class="jobs">
    <article class="job"><h4>Fusce sodales</h4><h5>Quisque gravida rhoncus</h5><p>Plan and support output projects with our clients, from first workshop to go-live and beyond.</p><a href="#">APPLY NOW</a></article>
    <article class="job"><h4>Vivamus iaculis</h4><h5>Quisque gravida rhoncus</h5><p>Build clean templates and interfaces for document creation and delivery in modern systems.</p><a href="#">APPLY NOW</a></article>
    <article class="job"><h4>Donec augue</h4><h5>Quisque gravida rhoncus</h5><p>Analyse business processes, gather requirements and turn them into clear technical concepts.</p><a href="#">APPLY NOW</a></article>
    <article class="job"><h4>Etiam sodales</h4><h5>Quisque gravida rhoncus</h5><p>Run trainings for customer teams and help users get the most from their new platform.</p><a href="#">APPLY NOW</a></article>
    <article class="job"><h4>Quisque tincidunt</h4><h5>Quisque gravida rhoncus</h5><p>Lead projects with care, keep budgets on track and bring every stakeholder along the way.</p><a href="#">APPLY NOW</a></article>
  </div>
  <a class="btn" href="#">VIEW ALL</a>
</section>

<section class="about">
  <h2 class="section-title">About Us</h2>
  <p class="lead">VelTarix is an IT consulting company from Germany specialised in output management. Our consultants bring years of experience from projects in banking, insurance, energy and the public sector. We believe in honest advice, solid craft and partnerships that last, and we measure our success by the success of our customers.</p>
  <a class="btn" href="#">READ MORE</a>
  <h3 class="staff-title">Our Staffs</h3>
  <div class="staff">
    <div class="member"><div class="member__photo" role="img" aria-label="Portrait photo of Daniel"></div><p class="member__name">DANIEL</p><p class="member__role">Software Engineer</p></div>
    <div class="member"><div class="member__photo" role="img" aria-label="Portrait photo of Sophia"></div><p class="member__name">SOPHIA</p><p class="member__role">Software Engineer</p></div>
    <div class="member"><div class="member__photo" role="img" aria-label="Portrait photo of Alexander"></div><p class="member__name">ALEXANDER</p><p class="member__role">Software Engineer</p></div>
    <div class="member"><div class="member__photo" role="img" aria-label="Portrait photo of Olivia"></div><p class="member__name">OLIVIA</p><p class="member__role">Software Engineer</p></div>
    <div class="member"><div class="member__photo" role="img" aria-label="Portrait photo of Jayden"></div><p class="member__name">JAYDEN</p><p class="member__role">Software Engineer</p></div>
    <div class="member"><div class="member__photo" role="img" aria-label="Portrait photo of Isabella"></div><p class="member__name">ISABELLA</p><p class="member__role">Software Engineer</p></div>
  </div>
</section>

<section class="contact">
  <h2 class="section-title">Contact Us</h2>
  <form class="form">
    <div class="form__row">
      <div class="field">First Name</div><div class="field">Last Name</div><div class="field">Email</div><div class="field">Phone</div>
    </div>
    <div class="field field--msg">Message</div>
    <span class="btn">SUBMIT</span>
  </form>
</section>

<footer class="site-footer">
  <div class="footer-col" style="left:140px">
    <h4>Links</h4>
    <div class="links"><span>Home</span><span>Partners</span><span>About Us</span><span>Career</span><span>Services</span><span>Contact</span></div>
  </div>
  <div class="footer-col" style="left:486px">
    <h4>Contact Info</h4>
    <p>Lindenweg 14, 70173 Stuttgart</p>
    <p>Phone: +49 711 480 2290</p>
    <p>Email: hello@veltarix.de</p>
  </div>
  <div class="footer-col" style="left:938px">
    <h4>Follow us on</h4>
    <div class="social"><span></span><span></span><span></span></div>
  </div>
  <p class="copyright">Copyright © 2019 VelTarix. All rights reserved.</p>
</footer>

</body>
</html>
```